Vindmark Health & Wellness needs a fresh and interesting website

I need a rebrand and redevelopment of my website, www.dellaquorne.example
Our mission is provide bespoke , lifestyle medicine , everyone has their own path to health. and we are creating a personalized experience for people to life their life to the fullest
Vindmark - means sea lands
I need an landing page and about page and potentially a few project launch pages , I have been using Wordpress for my basic information and then I use Plovix for the launch pages of my programs since I can edit those easily.

Target Market(s)

Corporate and individual's who are interested in a different perspective on health and wellness , and living with a chronic illness

Industry/Entity Type

Health, lifestyle , wellness coaching and medicine

Coding

Number of Pages Required

Font styles to use
Other font styles liked:
• look into the logo

Requirements
Must have
• the logo I uploaded
Nice to have
• I want a fresh perspective on health, I have bamboo, hibiscus vibes in my logo , but also like more of a water vibe/ I want something earthy but not too boho it needs to be clean
Should not have
• every other holistic health vibe,

```html
<!DOCTYPE html>
<html lang="en">
<head>
<meta charset="utf-8">
<title>About Me – Vindmark Health &amp; Wellness</title>
<link href="https://fonts.googleapis.com/css2?family=Playfair+Display:wght@700;800&family=Poppins:wght@400;500;600;700&family=Lora:ital,wght@1,500;1,600&display=swap" rel="stylesheet">
<style>
:root{
  --ink:#1f2a30;
  --body:#55606a;
  --teal:#17678a;
  --teal-dark:#0d5878;
  --sky:#1d8fb8;
  --green:#76b51a;
  --green-dark:#5f9612;
  --white:#ffffff;
  --mist:#f4f7f6;
  --sand:#d9914e;
  --bamboo:#8dbf4a;
  --footer:#0f668c;
  --footer-deep:#0b4f6d;
}
*{box-sizing:border-box;margin:0;padding:0}
html,body{width:1200px;height:2256px;overflow:hidden;background:var(--white)}
body{position:relative;font-family:"Poppins",sans-serif;color:var(--body)}
.abs{position:absolute}

/* header */
.site-header{left:0;top:0;width:1200px;height:72px}
.brand{left:44px;top:14px;display:flex;align-items:center;gap:10px}
.brand-dot{width:30px;height:30px;border-radius:50%;background:var(--teal)}
.brand-name{font-family:"Poppins",sans-serif;font-weight:600;font-size:17px;color:var(--teal);line-height:1.1;width:130px}
.nav{right:40px;top:26px;display:flex;gap:30px;align-items:center;font-size:12px;font-weight:600;letter-spacing:.5px;color:var(--ink)}
.nav .active{color:var(--green)}
.bamboo{left:0;top:80px;width:150px;height:260px;background:linear-gradient(160deg,#b8dc85,var(--bamboo) 60%,#5f8f2a);opacity:.8;border-radius:0 60px 60px 0}

.page-title{left:0;top:100px;width:1200px;text-align:center;font-family:"Playfair Display",serif;font-weight:800;font-size:92px;letter-spacing:2px;color:var(--teal)}

.desert{left:764px;top:322px;width:436px;height:436px;background:linear-gradient(180deg,#7bb9d9 0%,#b9d6e2 30%,#e4a866 48%,var(--sand) 70%,#b86d34 100%)}

.portrait{left:90px;top:468px;width:58px;height:58px;border-radius:50%;background:linear-gradient(135deg,#cfd6d9,#7c8890)}
.doc-name{left:162px;top:466px;font-family:"Playfair Display",serif;font-weight:700;font-size:34px;line-height:1.05;color:var(--ink)}
.doc-name span{display:block}

.copy{font-size:12.5px;line-height:1.75;color:var(--body)}
.copy p{margin-bottom:16px}
.copy-left{left:90px;top:566px;width:610px}
.copy-right{left:480px;top:904px;width:620px}

.woman{left:90px;top:846px;width:364px;height:364px;background:linear-gradient(180deg,#cfd8dc,#eef1f2 55%,#bfc8cc)}
.plant-right{left:1120px;top:1270px;width:80px;height:150px;background:linear-gradient(200deg,#9fd064,#4e8a22);border-radius:80px 0 0 80px}

/* quote + form */
.quote{left:112px;top:1388px;width:500px;font-family:"Lora",serif;font-style:italic;font-weight:500;font-size:22px;line-height:1.55;color:var(--ink)}
.quote b{font-weight:600}
.pot{left:418px;top:1616px;width:104px;height:150px;background:linear-gradient(180deg,#7fae5a 0%,#5d8c3c 50%,#e9ecec 52%,#d0d4d4 100%);border-radius:40px 40px 8px 8px}

.contact-form{left:680px;top:1370px;width:360px;height:510px;background:var(--green);padding:30px 28px}
.field-row{display:flex;gap:14px}
.field{flex:1;margin-bottom:16px}
.field label{display:block;font-size:10px;font-weight:600;color:var(--white);letter-spacing:.5px;margin-bottom:6px}
.field .box{background:var(--white);height:36px;font-size:11px;color:#9aa3a8;padding:10px 12px}
.field .box.tall{height:116px}
.submit{margin-top:6px;width:304px;height:40px;background:var(--sky);color:var(--white);font-weight:600;font-size:13px;letter-spacing:1px;display:flex;align-items:center;justify-content:center;gap:110px}

/* footer */
.footer-wave{left:0;top:1860px;width:1200px;height:80px}
.site-footer{left:0;top:1930px;width:1200px;height:290px;background:var(--footer)}
.foot-brand{left:170px;top:1944px;width:170px;display:flex;flex-direction:column;align-items:center;gap:10px}
.foot-brand .brand-dot{background:var(--white);width:44px;height:44px}
.foot-brand .brand-name{color:var(--white);text-align:center;width:170px;font-size:20px}
.socials{left:222px;top:2100px;display:flex;gap:14px}
.socials span{width:28px;height:28px;border-radius:50%;border:1.5px solid var(--white)}
.newsletter{left:504px;top:2004px;width:560px}
.newsletter h3{font-size:13px;font-weight:600;color:var(--white);letter-spacing:.5px;margin-bottom:12px}
.news-input{height:40px;border-bottom:1px solid rgba(255,255,255,.7);display:flex;justify-content:space-between;align-items:center;font-size:12px;color:rgba(255,255,255,.85);padding:0 6px}
.consent{margin-top:14px;margin-left:316px;font-size:10px;color:rgba(255,255,255,.8);display:flex;gap:6px;align-items:center}
.consent i{width:10px;height:10px;border:1px solid rgba(255,255,255,.8);display:inline-block}
.copyright{left:0;top:2220px;width:1200px;height:36px;background:var(--footer-deep);color:var(--white);font-size:10px;letter-spacing:1px;text-align:center;line-height:36px}
.to-top{left:1136px;top:2176px;width:34px;height:34px;border-radius:50%;background:var(--green);display:flex;align-items:center;justify-content:center}
</style>
</head>
<body>

<header class="abs site-header">
  <div class="abs brand"><span class="brand-dot"></span><span class="brand-name">Vindmark Health &amp; Wellness</span></div>
  <nav class="abs nav">
    <span>HOME</span><span class="active">ABOUT DELLA QUORNE</span><span>FALL RETREAT</span><span>CONTACT US</span>
    <svg width="16" height="16" viewBox="0 0 16 16" fill="none" stroke="#1f2a30" stroke-width="2"><circle cx="7" cy="7" r="5"/><path d="M11 11l4 4"/></svg>
  </nav>
</header>

<div class="abs bamboo" role="img" aria-label="Bamboo stalks and leaves"></div>

<h1 class="abs page-title">ABOUT ME</h1>

<div class="abs desert" role="img" aria-label="Photograph of desert sand dunes under a blue sky"></div>

<div class="abs portrait" role="img" aria-label="Small round portrait photo"></div>
<h2 class="abs doc-name"><span>DR DELLA QUORNE</span><span>DACM, L.AC.</span></h2>

<div class="abs copy copy-left">
  <p>At a young age, I discovered the transformative power of Eastern Medicine when it helped me overcome long, draining, persistent illness. It guided my attention to the body's quiet signals, showing me what real balance feels like, and it set me on a path toward the care I wanted to share with every patient and community I could reach.</p>
  <p>As an Eastern Medicine doctor, I've had the privilege of patiently supporting my community through integrative health choices. My journey began after years spent nurturing creativity and leadership; a holistic outlook grew when I made the life-altering decision to change my own life and pursue a degree in acupuncture and traditional East Asian medicine.</p>
  <p>Travel has profoundly healed me, and now I have the honor of using it to help others. With a Master's of Oriental Medicine and a Doctorate in Acupuncture and Integrative Medicine, I bring the highest level of expertise to my patients.</p>
</div>

<div class="abs woman" role="img" aria-label="Photograph of a woman in white with arms spread, seen from behind"></div>

<div class="abs copy copy-right">
  <p>I hold national certification in the field and am a licensed acupuncturist and doctor of Eastern Medicine. Beyond my academic achievements, I'm also an avid traveler, dedicated to bringing my best self to my patients and colleagues every day.</p>
  <p>When I'm off the clock, you'll find me immersed in nature, connecting with friends, mastering the tongue, practicing yoga and qi gong, sharing my heartfelt language studies, and savoring the rhythms of island dancing. I'm a devoted dog mom and take great pleasure in the ongoing adventure of remodeling our home.</p>
  <p>Join me on this journey of holistic healing, where we embrace and compassion converge to create a healthier, happier community. Let's explore the profound possibilities of Eastern Medicine together!</p>
</div>

<div class="abs plant-right" role="img" aria-label="Green tropical leaves"></div>

<blockquote class="abs quote">“In meditation you try and let go of the past. You try to stop being anxious about the future. You focus on and enjoy the time you have now. When you are stressed and burdened by things, it is liberating to tune into the present, to enter into the deeper rhythm of your being.” <b>Ewan Marlowe</b></blockquote>

<div class="abs pot" role="img" aria-label="Succulent plant in a white pot"></div>

<form class="abs contact-form">
  <div class="field-row">
    <div class="field"><label>FIRST NAME</label><div class="box">Enter your name</div></div>
    <div class="field"><label>LAST NAME</label><div class="box">Enter your name</div></div>
  </div>
  <div class="field"><label>EMAIL ADDRESS</label><div class="box">Enter email address</div></div>
  <div class="field"><label>SUBJECT</label><div class="box">Enter subject</div></div>
  <div class="field"><label>MESSAGE</label><div class="box tall">Type your message</div></div>
  <div class="submit"><span>SUBMIT</span>
    <svg width="14" height="14" viewBox="0 0 14 14" fill="#fff"><path d="M1 6L13 1 8 13 6.5 8z"/></svg>
  </div>
</form>

<svg class="abs footer-wave" viewBox="0 0 1200 80" preserveAspectRatio="none">
  <path d="M0 40 C300 0 700 10 1200 50 L1200 80 L0 80Z" fill="#2a8ab0"/>
  <path d="M0 70 C350 40 800 50 1200 72 L1200 80 L0 80Z" fill="#0f668c"/>
</svg>
<footer class="abs site-footer"></footer>
<div class="abs foot-brand"><span class="brand-dot"></span><span class="brand-name">Vindmark Health &amp; Wellness</span></div>
<div class="abs socials"><span></span><span></span></div>
<div class="abs newsletter">
  <h3>SUBSCRIBE NEWSLETTER</h3>
  <div class="news-input"><span>Enter your email address</span>
    <svg width="14" height="14" viewBox="0 0 14 14" fill="#fff"><path d="M1 6L13 1 8 13 6.5 8z"/></svg>
  </div>
  <div class="consent"><i></i>I agree to receive news by email</div>
</div>
<div class="abs to-top"><svg width="12" height="12" viewBox="0 0 12 12" fill="none" stroke="#fff" stroke-width="2"><path d="M2 8l4-4 4 4"/></svg></div>
<div class="abs copyright">COPYRIGHT © 2024 DELLA QUORNE. ALL RIGHTS RESERVED</div>

</body>
</html>
```